Hearing health care company needs a white paper redesigned to be more visually engaging

Thanks for your email. I'm looking for our white paper to be redesigned which would be used both digitally (on landing pages, emailed, etc.) and will be produced (printed) to be given out at tradeshows.
In it's current form, the white paper is very content heavy and light on visual elements. I provided a link within the brief to give designers an idea of what I'm looking for in terms of transforming the paper into something more visually engaging, which could mean less text on each page using more images on pages, call outs, etc. Here's the link I provided in the brief: http://images.solutions.quorvantex.example/Web/Quorvantex/%7B177f9703-1295-48cf-b64f-a12259a04a1b%7D_Playbook_Carewise_Bulletin_Approved_Web_File_05.31.2019.pdf
We need our white paper on state mandated benefits redesigned (background is we had to rush to get our final copy in layout and design and produced it quickly to send to a conference. Now that we have some time, we'd like to have it designed correctly so we can distribute it more broadly and so it's more visually engaging). All of the content and copy needs to remain as is in the attached document but instead of it appearing so copy heavy, would like to see new options for a redesigned white paper that's more visually appealing. Here's an example/inspiration for this redesign: http://images.solutions.quorvantex.example/Web/Quorvantex/%7B177f9703-1295-48cf-b64f-a12259a04a1b%7D_Playbook_Carewise_Bulletin_Approved_Web_File_05.31.2019.pdf
I love the layout and images they use on every page vs. our paper that is heavy on content. I'm okay with more pages as I think in this format, the content will be more digestible and engaging.
Background on Veltoria Hearing Health Care:
Veltoria serves as a trusted advocate to over 300 client partners, making hearing health care simple by delivering turnkey products and services that improve health, increase satisfaction and lower costs. As an independently owned and operated organization, we act in our partners’ best interests in everything we do.
The Veltoria Hearing Health Care Difference:
-Simplicity - We do the heavy lifting to implement, administer
and customize our turnkey products and services to meet the
unique needs of your organization
-Value - Our full-service hearing benefit solutions help address
social determinants of health that contribute to high cost
health conditions, while delivering an exceptional member
experience
-Trust & Advocacy - As an industry expert who is not
owned by a manufacturer, we are uniquely positioned to
serve as your trusted advocate, committed to always acting
in your best interest
For more information about Veltoria Hearing Health Care, visit: veltoriausa.example/healthplans. This is our health plan site where our health plan prospects are visiting (Pages include: Why a Hearing Benefit, Choosing a Partner, Working with Veltoria, Plan Choices). If you click on "For Members," this will take you to our consumer-facing site.
Where would this white paper live and who are we sending it to?
This file would live in our content library so our team, primarily our sales team could send it to health plans (our target market) key decision makers (think executives and managers) in addition to distributing it to industry partners (like National Coverage Providers Guild (NCPG) and other organizations to be included on their website, sent to their health plan stakeholders, included as an insert in health care publications (i.e. Benefit Ledger)) . Additionally, we have a blog post already written to promote this white paper, driving people to a landing page to download it and will eventually be included in our resource center on our website (http://go.veltoriausa.example/the-hearing-benefit-resource-center).
Imagery direction:
-Would like to see images of a diverse group of people in terms of race, sex and age
-Images don't need to include only older people - image of grandparents/ adults with young kids in the photos are fine - we actually like to use multi-generational photos in our materials (check out our website for more info and to see the images we use: https://www.veltoriausa.example/. Additionally, here's a link to our B2B blog that may help with regard to seeing what type of images we like to use: http://blog.veltoriausa.example/partners). I've attached a medicare advantage deck that includes imagery as an example and to see how our brand guidelines are used in a presentation - this deck is created for a very important part of the health plan audience we are targeting - FYI see deck for more context.)
-I've included the map JPG file as seen on page 7
-I've attached many of our stock images that we've purchased that we use if you would like to use these, which is optional.
-I've also attached a couple icons that you can use. I've included the master pages of the icons that we have for our brand. Just let me know if you need any. Didn't want to send them all over.
I've attached our brand guidelines, fonts and logos.
Note: Veltoria is our parent company so even in the brand guidelines they show the logo as Veltoria, ours is Veltoria Hearing Health Care. We also don't use green as an overall color or background nor the green gradient (which is more of a teal) as that is our sister company's color (Sonabright).
File needs/packaging: Need packaged InDesign files, link images AND include as separate files; ensure colors, fonts and logos match Veltoria Hearing Health Care brand guidelines (not our parent company Veltoria). Thank you and please let me know if any questions come up or you are in need of any other files.

```html
<!DOCTYPE html>
<html lang="en">
<head>
<meta charset="utf-8">
<title>State-Mandated Expansion of Hearing Health Care Coverage — White Paper Layout</title>
<link href="https://fonts.googleapis.com/css2?family=Poppins:wght@400;500;600;700&display=swap" rel="stylesheet">
<style>
  :root {
    --backdrop: #e8e8e9;
    --paper: #ffffff;
    --magenta: #e3195a;
    --magenta-deep: #c4145a;
    --plum: #7a1f6e;
    --ink: #3a3a3c;
    --ink-soft: #6b6b70;
    --leaf-dark: #2f5a2a;
    --leaf-mid: #5f8a3c;
    --leaf-light: #b7cf8a;
    --warm-photo: #8a6a4c;
  }
  * { box-sizing: border-box; margin: 0; padding: 0; }
  html, body { width: 1200px; height: 900px; overflow: hidden; }
  body {
    background: var(--backdrop);
    font-family: "Poppins", "Helvetica Neue", Arial, sans-serif;
    color: var(--ink);
    position: relative;
  }

  /* ---------- Cover ---------- */
  .cover {
    position: absolute;
    left: 110px; top: 210px;
    width: 370px; height: 480px;
    background: linear-gradient(155deg, var(--magenta) 0%, var(--magenta-deep) 45%, var(--plum) 100%);
    box-shadow: 0 6px 18px rgba(0,0,0,.18);
    color: #fff;
    overflow: hidden;
  }
  .cover__texture {
    position: absolute;
    right: -40px; top: 150px;
    width: 300px; height: 300px;
    background: radial-gradient(circle at 55% 45%, rgba(120,40,140,.55) 0%, rgba(120,40,140,.2) 45%, rgba(120,40,140,0) 70%);
  }
  .cover__brand {
    position: absolute; right: 30px; top: 30px;
    display: flex; align-items: center; gap: 6px;
    font-size: 13px; font-weight: 600; letter-spacing: .2px;
  }
  .cover__brand-mark { width: 8px; height: 8px; background: #fff; border-radius: 50%; }
  .cover__title {
    position: absolute; left: 32px; top: 92px; width: 300px;
    font-size: 27px; line-height: 1.12; font-weight: 700;
  }
  .cover__subtitle {
    position: absolute; left: 32px; top: 232px; width: 280px;
    font-size: 12px; line-height: 1.35; font-weight: 400;
  }

  /* ---------- Spreads ---------- */
  .spread {
    position: absolute;
    width: 540px; height: 350px;
    display: flex;
    box-shadow: 0 6px 16px rgba(0,0,0,.16);
    background: var(--paper);
  }
  .spread--contents { left: 620px; top: 50px; }
  .spread--intro { left: 620px; top: 480px; }
  .page { position: relative; width: 270px; height: 350px; overflow: hidden; }
  .page--left { box-shadow: inset -6px 0 8px -6px rgba(0,0,0,.18); }
  .page--right { box-shadow: inset 6px 0 8px -6px rgba(0,0,0,.12); }

  /* Contents spread */
  .contents__photo {
    position: absolute; inset: 0;
    background:
      radial-gradient(ellipse at 78% 18%, rgba(235,240,200,.9) 0%, rgba(235,240,200,0) 35%),
      radial-gradient(ellipse at 30% 55%, rgba(205,190,175,.85) 0%, rgba(205,190,175,0) 30%),
      linear-gradient(180deg, var(--leaf-mid) 0%, var(--leaf-dark) 55%, #44632f 100%);
  }
  .contents__panel {
    position: absolute; right: 0; top: 0;
    width: 230px; height: 350px;
    background: rgba(255,255,255,.55);
    padding: 80px 18px 0 22px;
  }
  .contents__title {
    color: var(--magenta); font-size: 17px; line-height: 1.1; font-weight: 600;
    margin-bottom: 16px;
  }
  .contents__list { list-style: none; }
  .contents__item {
    display: flex; align-items: flex-end; gap: 6px;
    font-size: 6px; line-height: 1.35; color: var(--ink);
    margin-bottom: 8px;
  }
  .contents__label { width: 95px; }
  .contents__leader { flex: 1; border-bottom: 1px dotted var(--ink-soft); margin-bottom: 2px; }
  .contents__num { width: 8px; text-align: right; }

  /* Intro spread */
  .intro__heading {
    position: absolute; left: 16px; top: 14px;
    color: var(--magenta); font-size: 13px; font-weight: 600;
  }
  .intro__photo {
    position: absolute; top: 62px; height: 200px;
    background:
      radial-gradient(ellipse at 60% 40%, rgba(120,90,70,.85) 0%, rgba(120,90,70,0) 40%),
      linear-gradient(160deg, #6e8a3f 0%, var(--leaf-dark) 55%, var(--warm-photo) 100%);
  }
  .intro__photo--left { left: 90px; right: 0; }
  .intro__photo--right { left: 0; width: 74px;
    background:
      radial-gradient(ellipse at 10% 45%, rgba(140,100,80,.8) 0%, rgba(140,100,80,0) 55%),
      linear-gradient(160deg, #5b7c35 0%, var(--leaf-dark) 55%, var(--warm-photo) 100%);
  }
  .col {
    position: absolute; top: 62px;
    font-size: 3.6px; line-height: 1.45; color: var(--ink);
  }
  .col p { margin-bottom: 4px; }
  .col--a { left: 16px; width: 66px; }
  .col--b { left: 80px; width: 66px; }
  .col--c { left: 156px; width: 96px; }
  .pull {
    font-size: 6.2px; line-height: 1.35; color: var(--ink-soft);
    margin: 2px 0 6px;
  }
  .callout {
    border-top: 1px solid var(--magenta);
    padding-top: 4px; margin-bottom: 6px;
    color: var(--magenta); font-size: 6px; line-height: 1.25; font-weight: 500;
  }
  .col--c ul { padding-left: 6px; }
  .col--c li { margin-bottom: 3px; }
  .folio {
    position: absolute; bottom: 12px; left: 16px; right: 16px;
    border-top: 1px solid var(--magenta);
    padding-top: 3px;
    display: flex; justify-content: space-between;
    font-size: 3.4px; color: var(--magenta);
  }
</style>
</head>
<body>

  <!-- Cover -->
  <section class="cover">
    <div class="cover__texture" role="img" aria-label="Soft field of scattered purple dots fading across the cover"></div>
    <div class="cover__brand"><span class="cover__brand-mark"></span>Veltoria Hearing Health Care</div>
    <h1 class="cover__title">State-Mandated Expansion of Hearing Health Care Coverage</h1>
    <p class="cover__subtitle">A response to the growing prevalence of hearing loss in children and adults</p>
  </section>

  <!-- Contents spread -->
  <section class="spread spread--contents">
    <div class="page page--left">
      <div class="contents__photo" role="img" aria-label="Photo of a laughing grandmother riding piggyback on a grandfather outdoors among green trees"></div>
    </div>
    <div class="page page--right">
      <div class="contents__photo" role="img" aria-label="Continuation of the outdoor photo with sunlit green foliage" style="background: radial-gradient(ellipse at 50% 15%, rgba(235,240,200,.9) 0%, rgba(235,240,200,0) 40%), linear-gradient(180deg, var(--leaf-light) 0%, var(--leaf-mid) 50%, var(--leaf-dark) 100%);"></div>
      <div class="contents__panel">
        <h2 class="contents__title">Table of<br>Contents</h2>
        <ol class="contents__list">
          <li class="contents__item"><span class="contents__label">Introduction</span><span class="contents__leader"></span><span class="contents__num">1</span></li>
          <li class="contents__item"><span class="contents__label">The adverse impacts of hearing loss at every stage of life</span><span class="contents__leader"></span><span class="contents__num">2</span></li>
          <li class="contents__item"><span class="contents__label">State mandates and the challenges for health insurers</span><span class="contents__leader"></span><span class="contents__num">3</span></li>
          <li class="contents__item"><span class="contents__label">Achieving cost containment while ensuring high-quality care</span><span class="contents__leader"></span><span class="contents__num">4</span></li>
          <li class="contents__item"><span class="contents__label">10 benchmarks for finding the right hearing health care partner</span><span class="contents__leader"></span><span class="contents__num">5</span></li>
          <li class="contents__item"><span class="contents__label">Key takeaways</span><span class="contents__leader"></span><span class="contents__num">6</span></li>
          <li class="contents__item"><span class="contents__label">About Veltoria Hearing Health Care</span><span class="contents__leader"></span><span class="contents__num">7</span></li>
          <li class="contents__item"><span class="contents__label">Sources</span><span class="contents__leader"></span><span class="contents__num">8</span></li>
        </ol>
      </div>
    </div>
  </section>

  <!-- Introduction spread -->
  <section class="spread spread--intro">
    <div class="page page--left">
      <h2 class="intro__heading">Introduction</h2>
      <div class="col col--a">
        <p>Just a few years ago, the health insurance industry was grappling with mandated hearing health care coverage under the Affordable Care Act (ACA). Starting in 2017, the ACA expanded hearing aid coverage under the concept of “essential health benefits” (EHBs), and in many states it eliminated dollar, age and/or frequency restrictions.</p>
        <p>Since then, of course, the health care insurance landscape has shifted dramatically, stemming from much uncertainty over the future of ACA mandates.</p>
        <p class="pull">Meanwhile, the prevalence of hearing loss continues to grow, attributable to a number of factors, including exposure to damaging noise and a rapidly aging population. Yet there’s a large and widening gap between the need for hearing health care services and the number of people who actually receive it.</p>
        <p>Exacerbating matters, a mounting body of research proves that hearing loss affects much more than just the ability to perceive</p>
      </div>
      <div class="intro__photo intro__photo--left" role="img" aria-label="Photo of a young girl whispering into her smiling grandfather's ear on a park bench"></div>
      <div class="folio"><span>1</span><span>State-Mandated Expansion of Hearing Health Care Coverage</span></div>
    </div>
    <div class="page page--right">
      <div class="intro__photo intro__photo--right" role="img" aria-label="Continuation of the park bench photo across the gutter"></div>
      <div class="col col--b">
        <p>sound — it’s a risk factor for a variety of physical, emotional and developmental issues for both children and adults.</p>
        <p>For children, a hearing impairment can lead to a number of negative consequences, including delayed development of speech and language skills, poor academic performance and behavioral issues. In adults, untreated hearing loss significantly elevates the risk of cognitive decline, dementia, social isolation, depression and injury-causing falls.</p>
        <p>As these hearing loss comorbidities come into sharper focus, the importance of early diagnosis and intervention of hearing loss has become equally clear. In response, at least 23 states have mandated some form of coverage by qualified health plans (QHPs) for hearing aids and ancillary services.</p>
        <p>A majority of state mandates apply to hearing health care services for children. However, just as the ACA started to eliminate age restrictions for hearing aid coverage as an EHB, a number of states have mandated coverage regardless of age. Across the country, the lesson learned is this: Addressing hearing loss delivers substantial benefits, whether it’s enabling healthy development and a lifetime of learning for children or preventing serious and costly health conditions in adults.</p>
      </div>
      <div class="col col--c">
        <p class="callout">How do you comply with mandated coverage requirements while reducing risks, controlling costs, and ensuring the long-term viability of your organization?</p>
        <p>The fundamental question for those who oversee health plans: “How do you comply with mandated coverage requirements while reducing risks, controlling costs, and ensuring the long-term viability of your organization?” This white paper will discuss these seemingly incongruous objectives from a number of perspectives:</p>
        <ul>
          <li>The prevalence and adverse impacts of hearing loss at every stage of life</li>
          <li>State mandates and the challenges for health insurance carriers, both logistical and financial</li>
          <li>Ensuring access to patient-centered, high-quality hearing health care services and, at the same time, containing costs through the use of narrow provider networks and product formularies</li>
          <li>How to find the right partner that can assume much of the burden of implementing and managing a hearing health care program</li>
        </ul>
      </div>
      <div class="folio"><span>State-Mandated Expansion of Hearing Health Care Coverage</span><span>2</span></div>
    </div>
  </section>

</body>
</html>
```